Group Medical Practice needs stationery, business cards etc. designed

We need stationery designed for a multisite practice that offers primary medical, dental and behavioral healthcare. We would like a design that is consistent for letterhead, business cards, Microsoft Outlook stationery etc. We have attached our new logo design.

Business

```html
<!DOCTYPE html>
<html lang="en">
<head>
<meta charset="utf-8">
<title>Ridgeline Care Group – Envelope</title>
<link rel="stylesheet" href="https://fonts.googleapis.com/css2?family=Arimo:wght@400&display=swap">
<style>
  :root {
    --page-bg: #f7f7f7;
    --paper: #ffffff;
    --sky-blue: #dce8f2;
    --sky-edge: #c3d6e6;
    --brand-blue: #1f6fb5;
    --rule-grey: #d9d9d9;
    --text-grey: #555555;
  }
  html, body {
    margin: 0;
    padding: 0;
    width: 1200px;
    height: 1000px;
    overflow: hidden;
    background: var(--page-bg);
    font-family: "Arimo", Arial, sans-serif;
  }
  .envelope {
    position: absolute;
    left: 217px;
    top: 322px;
    width: 763px;
    height: 388px;
    background: var(--paper);
    box-shadow: 6px 8px 10px rgba(0, 0, 0, 0.18);
  }
  .corner-backdrop {
    position: absolute;
    left: 0;
    top: 0;
    width: 240px;
    height: 140px;
  }
  .brand {
    position: absolute;
    left: 16px;
    top: 124px;
    width: 200px;
    display: flex;
    align-items: center;
    justify-content: center;
    gap: 7px;
  }
  .brand-mark {
    width: 10px;
    height: 10px;
    border-radius: 50%;
    background: var(--brand-blue);
  }
  .brand-name {
    margin: 0;
    font-size: 15px;
    font-weight: 400;
    letter-spacing: 0.4px;
    color: var(--brand-blue);
    white-space: nowrap;
  }
  .divider {
    position: absolute;
    left: 23px;
    top: 168px;
    width: 198px;
    height: 1px;
    background: var(--rule-grey);
  }
  .return-address {
    position: absolute;
    left: 33px;
    top: 184px;
    margin: 0;
    font-style: normal;
    font-size: 13px;
    line-height: 16px;
    color: var(--text-grey);
    white-space: nowrap;
  }
</style>
</head>
<body>
  <div class="envelope">
    <svg class="corner-backdrop" viewBox="0 0 240 140" role="img" aria-label="Soft blue sky fading into a snowy mountain range">
      <defs>
        <linearGradient id="sky-fade" x1="0" y1="0" x2="0" y2="1">
          <stop offset="0" stop-color="#dce8f2"/>
          <stop offset="0.45" stop-color="#dce8f2"/>
          <stop offset="0.78" stop-color="#f3f7fb"/>
          <stop offset="1" stop-color="#ffffff"/>
        </linearGradient>
      </defs>
      <polygon points="0,0 173,0 236,138 0,138" fill="url(#sky-fade)"/>
      <rect x="0" y="0" width="173" height="2" fill="var(--sky-edge)"/>
    </svg>
    <div class="brand">
      <span class="brand-mark"></span>
      <p class="brand-name">Ridgeline Care Group</p>
    </div>
    <div class="divider"></div>
    <address class="return-address">
      240 Cedar Hollow Road Ste 110<br>
      Laurel Falls, Virginia 24301
    </address>
  </div>
</body>
</html>
```